Brookfern Dental Brochure

Most of the information is on the existing brochure, I just think the layout needs to be cleaner and more modern. I tend to like a darker brochure with white or light grey text (it also looks great with our new logo - also attached). The finished brochure should been in a format that I can send to pelmo press and also edit myself if the text needs to change.

Besides the info in the attached scan, I'd also like to include at-home custom fit whitening kits for $89. I am also looking for a new motto. It is currently "Quality Dentistry, Affordable Prices"

The web address has been changed to BrookfernDentalOzark.com and the email address is Info@BrookfernDentalOzark.com

I'd like to re-draw the maps as well. Our Hot Springs location is here:

https://www.plotvane.com/maps/place/2870+Wexley+Ave,+Hot+Springs+National+Park,+AR+71901/@34.512817,-93.041362,17z/data=!3m1!4b1!4m2!3m1!1s0x11aa2b3cc4d5e678:0x9f8e7d6c5b4a3921

Little Rock location:

https://www.plotvane.com/maps/place/9845+Marrow+Fenn+Rd+%234400,+Little+Rock,+AR+72210/@34.7209854,-92.398213,17z/data=!3m1!4b1!4m2!3m1!1s0x22bb3c4dd5e6f789:0x1a2b3c4d5e6f7081

Target Market(s)

Anyone who is interested in general dentistry except for young children. We currently see a lot of low income patients and retirees. We would like to expand that market.

Industry/Entity Type

Dental

Font styles to use
Other font styles liked:
• I don't know the name of the font but I like the one used in the logo

Requirements
Must have
• A catchy design - especially on the front page. We want people to pick them up and browse.
Nice to have
• I love ultra modern design. Minimalist. Sleek.
Should not have
• clashing colors like the current brochure. We're going for catchy but not cheezy.

```html
<!DOCTYPE html>
<html lang="en">
<head>
<meta charset="utf-8">
<title>Brookfern Dental Brochure</title>
<link href="https://fonts.googleapis.com/css2?family=Quicksand:wght@400;500;600&family=Montserrat:wght@300;500;600&display=swap" rel="stylesheet">
<style>
  :root {
    --backdrop: #e8e8e8;
    --page: #3e3f42;
    --page-deep: #333437;
    --ink: #f1f1f1;
    --ink-soft: #c4c6ca;
    --accent: #3d8fdb;
    --accent-deep: #1f5fa8;
    --map-light: #e3e1da;
    --map-mid: #cfcbc0;
  }
  * { box-sizing: border-box; margin: 0; padding: 0; }
  html, body { width: 1200px; height: 941px; overflow: hidden; }
  body {
    background: var(--backdrop);
    font-family: "Quicksand", sans-serif;
    color: var(--ink);
    position: relative;
  }
  .spread {
    position: absolute; left: 110px; top: 95px;
    width: 980px; height: 750px;
    display: flex;
    box-shadow: 0 14px 40px rgba(0,0,0,.25);
  }
  .page {
    width: 490px; height: 100%;
    background: linear-gradient(90deg, var(--page) 0%, var(--page) 88%, var(--page-deep) 100%);
    padding: 34px 34px 30px;
    position: relative;
    font-size: 9.5px; line-height: 1.45;
  }
  .page--right { background: linear-gradient(90deg, var(--page-deep) 0%, var(--page) 12%, var(--page) 100%); }

  .brand { display: flex; align-items: center; gap: 10px; }
  .brand__mark { width: 14px; height: 14px; background: var(--accent); }
  .brand__name {
    font-family: "Montserrat", sans-serif; font-weight: 300;
    font-size: 30px; letter-spacing: 2px; text-transform: uppercase; color: var(--ink);
  }
  .tagline {
    font-family: "Montserrat", sans-serif; font-weight: 600; font-size: 10px;
    letter-spacing: 1px; text-transform: uppercase; margin-top: 6px; color: var(--ink);
  }

  .contacts { display: flex; gap: 40px; margin-top: 18px;
    font-family: "Montserrat", sans-serif; font-weight: 600; font-size: 9px; text-transform: uppercase; }

  .section-title {
    font-family: "Montserrat", sans-serif; font-weight: 300; font-size: 20px;
    text-transform: uppercase; letter-spacing: 1px; margin: 20px 0 6px;
  }
  .service-group { margin-bottom: 5px; }
  .service-group__head {
    font-family: "Montserrat", sans-serif; font-weight: 600; text-transform: uppercase;
    font-size: 10px; display: flex; align-items: center; gap: 6px;
  }
  .service-group__head::after { content: ""; width: 8px; height: 8px; background: var(--accent); }
  .price-row { display: grid; grid-template-columns: 150px 1fr; color: var(--ink-soft); }
  .services { columns: 2; column-gap: 30px; }
  .services .service-group { break-inside: avoid; }

  .note {
    margin-top: 10px; font-family: "Montserrat", sans-serif; font-weight: 600;
    font-size: 8.5px; text-transform: uppercase; line-height: 1.5;
  }
  .note__mark { display: inline-block; width: 8px; height: 8px; background: var(--accent); vertical-align: middle; }
  .web { margin-top: 10px; font-family: "Montserrat", sans-serif; font-size: 9px; text-transform: uppercase; letter-spacing: .5px; }

  .maps { position: absolute; left: 34px; right: 34px; bottom: 30px; display: flex; gap: 22px; }
  .map { flex: 1; background: #f4f4f4; padding: 6px; }
  .map__area { height: 120px; background: linear-gradient(135deg, var(--map-light), var(--map-mid)); }
  .map__caption { font-family: "Montserrat", sans-serif; font-weight: 600; font-size: 8px; color: #333; margin-top: 5px; }

  .label {
    display: inline-block; background: linear-gradient(90deg, var(--accent-deep), var(--accent));
    color: #fff; font-family: "Montserrat", sans-serif; font-weight: 600; font-size: 9px;
    text-transform: uppercase; letter-spacing: .5px; padding: 4px 10px; margin: 12px 0 5px;
  }
  .price-table { margin-top: 12px; display: grid; grid-template-columns: 80px 70px 70px; gap: 2px 0; font-size: 9px; color: var(--ink-soft); }
  .price-table__head { font-family: "Montserrat", sans-serif; font-weight: 600; font-size: 7.5px; color: var(--ink); text-transform: uppercase; }
  .columns { display: grid; grid-template-columns: 1fr 1fr; gap: 26px; }
  .body-copy { color: var(--ink-soft); }
  .feature-box {
    margin-top: 14px; background: linear-gradient(160deg, var(--accent), var(--accent-deep));
    padding: 12px; color: #fff; font-size: 9px;
  }
</style>
</head>
<body>
<main class="spread">
  <section class="page page--left">
    <div class="brand"><span class="brand__mark"></span><span class="brand__name">Brookfern Dental</span></div>
    <p class="tagline">Quality Dentistry · Affordable Prices</p>

    <div class="contacts">
      <address>501 / 555-0142<br>2870 Wexley Avenue<br>Hot Springs, Arkansas</address>
      <address>501 / 555-0178<br>9845 Marrow Fenn Road<br>Suite 4400<br>Little Rock, Arkansas</address>
    </div>

    <h2 class="section-title">Other Services</h2>
    <div class="services">
      <div class="service-group">
        <div class="service-group__head">Exams</div>
        <div class="price-row"><span>Limited (problem focused)</span><span>$40</span></div>
        <div class="price-row"><span>Comprehensive</span><span>$50</span></div>
        <div class="price-row"><span>Periodic (yearly)</span><span>$38</span></div>
      </div>
      <div class="service-group">
        <div class="service-group__head">X-Rays</div>
        <div class="price-row"><span>Single</span><span>$25</span></div>
        <div class="price-row"><span>Full mouth</span><span>$75</span></div>
        <div class="price-row"><span>Bite wings (2)</span><span>$40</span></div>
      </div>
      <div class="service-group">
        <div class="service-group__head">Extraction · Requires X-Ray</div>
        <div class="price-row"><span>Simple</span><span>$90</span></div>
        <div class="price-row"><span>Surgical (more involved)</span><span>$150</span></div>
      </div>
      <div class="service-group">
        <div class="service-group__head">Denture Repair</div>
        <div class="price-row"><span>Simple</span><span>$75</span></div>
        <div class="price-row"><span>With impression</span><span>$100+up</span></div>
      </div>
      <div class="service-group">
        <div class="service-group__head">Crowns</div>
        <div class="price-row"><span>Cast metal</span><span>$650</span></div>
        <div class="price-row"><span>Porcelain metal</span><span>$750</span></div>
        <div class="price-row"><span>Porcelain</span><span>$850</span></div>
        <div class="price-row"><span>Gold</span><span>$650 + gold</span></div>
      </div>
      <div class="service-group">
        <div class="service-group__head">Hygiene Services</div>
        <div class="price-row"><span>Routine cleaning</span><span>$65</span></div>
        <div class="price-row"><span>Full mouth debridement</span><span>$85</span></div>
        <div class="price-row"><span>At-home whitening kit</span><span>$89</span></div>
      </div>
    </div>

    <p class="note">Smile Credit is an affordable option for financing your dental work. Please inquire — otherwise payment is expected when services are rendered <span class="note__mark"></span></p>
    <p class="web">Info@BrookfernDentalOzark.com<br>brookferngroup@mailhaven.net<br>www.BrookfernDentalOzark.com</p>

    <div class="maps">
      <figure class="map">
        <div class="map__area" role="img" aria-label="Street map showing the Hot Springs office on Wexley Avenue"></div>
        <figcaption class="map__caption">2870 Wexley Avenue, Hot Springs, Arkansas</figcaption>
      </figure>
      <figure class="map">
        <div class="map__area" role="img" aria-label="Street map showing the Little Rock office on Marrow Fenn Road"></div>
        <figcaption class="map__caption">9845 Marrow Fenn Road, Little Rock, Arkansas</figcaption>
      </figure>
    </div>
  </section>

  <section class="page page--right">
    <div class="brand"><span class="brand__mark"></span><span class="brand__name">Brookfern Dental</span></div>
    <span class="label">Dentures</span>
    <div class="price-table">
      <span></span><span class="price-table__head">Upper or Lower</span><span class="price-table__head">Upper &amp; Lower</span>
      <span>Standard</span><span>$400</span><span>$700</span>
      <span>Premium</span><span>$550</span><span>$1000</span>
      <span>Elite</span><span>$700</span><span>$1300</span>
      <span>Super Elite</span><span>$850</span><span>$1600</span>
    </div>

    <div class="columns">
      <div>
        <span class="label">Standard · Most Economical</span>
        <p class="body-copy">A basic, well-fitting denture built for comfort and function with simple, natural-looking teeth at a modest price.</p>
        <span class="label">Premium · Cosmetic Approval</span>
        <p class="body-copy">You see and approve a wax try-in before final processing, so the shape and shade of your new teeth look right.</p>
        <span class="label">Elite · Most Popular</span>
        <p class="body-copy">Higher quality teeth with lifelike shading and a custom gum tone, chosen together with you for a natural smile.</p>
        <span class="label">Super Elite · Our Best</span>
        <p class="body-copy">Our finest denture with premium layered teeth, detailed gum contouring and extra fittings for the most natural result.</p>
      </div>
      <div>
        <span class="label">Dentures with Extractions</span>
        <p class="body-copy">Teeth are removed and the denture placed the same day, so you never leave without a smile while healing.</p>
        <span class="label">Treatment Dentures · $350 per arch</span>
        <p class="body-copy">A temporary denture worn during healing before your permanent set is made.</p>
        <span class="label">Relines</span>
        <p class="body-copy">In office · $150 per arch<br>Lab processed · $175 per arch</p>
        <span class="label">Partial Dentures</span>
        <p class="body-copy">Acrylic partials · $300 / arch<br>Cast metal partials · $900 / arch<br>Clear clasp partials · $1300 / arch</p>
        <div class="feature-box">Clear clasp partials blend with your natural teeth and gums, with no visible metal for a discreet, comfortable fit.</div>
      </div>
    </div>
  </section>
</main>
</body>
</html>
```